Criação de Papelaria (6 itens) para Arquitetura
" Sou recém formada em Design de Interiores e pretendo começar a divulgar meu negócio. Já fiz alguns trabalhos / projetos, mas ainda não consegui alavancar minha marca. Meu foco será a realização de projetos residenciais, comerciais e empresariais. As atividades vão desde a entrevista inicial para entendimento das necessidades do cliente, passando pela preparação dos projetos com imagens renderizadas, plantas baixas, projetos de marcenaria, iluminação, gesso etc., incluindo também acompanhamento a lojas para escolha de materiais / móveis até o acompanhamento da obra e fiscalização dos trabalhos executados por terceiros. "

```html
<!DOCTYPE html>
<html lang="pt-BR">
<head>
<meta charset="utf-8">
<title>Lia Moreira — Cartões de Visita</title>
<link rel="stylesheet" href="https://fonts.googleapis.com/css2?family=Roboto+Condensed:wght@400;700&family=Raleway:wght@300;400&display=swap">
<style>
  :root {
    --stage: #2a2a2d;
    --card-dark: #45404f;
    --card-dark-deep: #2f2b37;
    --rose: #e7ab9c;
    --rose-light: #f6cfc3;
    --rose-deep: #c98a7c;
    --ink-light: #ffffff;
    --ink-soft: #d9d4de;
  }
  * { margin: 0; padding: 0; box-sizing: border-box; }
  html, body { width: 1200px; height: 1200px; overflow: hidden; }
  body { background: var(--stage); position: relative; font-family: "Roboto Condensed", sans-serif; }

  .card {
    position: absolute;
    top: 511px;
    width: 518px;
    height: 252px;
    border-radius: 24px;
    overflow: hidden;
  }

  /* Contact side */
  .card--contact {
    left: 67px;
    background: linear-gradient(180deg, var(--card-dark) 0%, var(--card-dark-deep) 100%);
  }
  .contact__band {
    position: absolute; left: 0; top: 0; width: 100%; height: 108px;
    background: linear-gradient(90deg, var(--rose-light) 0%, var(--rose) 55%, var(--rose-deep) 100%);
  }
  .contact__brand {
    position: absolute; left: 0; width: 100%; top: 42px;
    text-align: center;
    font-family: "Raleway", sans-serif; font-weight: 400;
    font-size: 18px; letter-spacing: 5px; color: var(--ink-light);
  }
  .contact__name {
    position: absolute; left: 29px; top: 136px;
    font-weight: 700; font-size: 27px; color: var(--ink-light);
  }
  .contact__role {
    position: absolute; left: 30px; top: 168px;
    font-weight: 400; font-size: 14px; color: var(--ink-soft);
  }
  .contact__list { position: absolute; list-style: none; }
  .contact__list--direct { left: 223px; top: 140px; }
  .contact__list--social { left: 390px; top: 144px; }
  .contact__item {
    display: flex; align-items: center; gap: 9px;
    font-size: 14px; color: var(--ink-soft); height: 21px;
  }
  .contact__list--social .contact__item { margin-bottom: 20px; }
  .contact__item--email { margin-top: 20px; }
  .contact__icon { width: 20px; height: 20px; flex: none; }
  .contact__phones { display: flex; flex-direction: column; line-height: 19px; font-size: 13px; }

  /* Brand side */
  .card--brand {
    left: 612px;
    background: linear-gradient(160deg, #514b5c 0%, var(--card-dark) 45%, var(--card-dark-deep) 100%);
  }
  .brand__mark {
    position: absolute; left: 241px; top: 30px;
    width: 34px; height: 34px; background: var(--rose);
  }
  .brand__name {
    position: absolute; left: 0; width: 100%; top: 100px;
    text-align: center;
    font-family: "Raleway", sans-serif; font-weight: 300;
    font-size: 42px; letter-spacing: 5px; color: var(--rose);
  }
  .brand__tagline {
    position: absolute; left: 0; width: 100%; top: 150px;
    text-align: center;
    font-family: "Raleway", sans-serif; font-weight: 400;
    font-size: 10px; letter-spacing: 5px; color: var(--rose);
  }
  .brand__rule {
    position: absolute; left: 6px; right: 0; top: 202px; height: 3px;
    background: linear-gradient(90deg, var(--rose-deep), var(--rose-light) 60%, var(--rose));
  }
</style>
</head>
<body>

<section class="card card--contact">
  <div class="contact__band" role="img" aria-label="Faixa rosé com textura de grade fina"></div>
  <div class="contact__brand">LIA MOREIRA</div>
  <h1 class="contact__name">Lia Moreira</h1>
  <p class="contact__role">Designer de Interiores</p>

  <ul class="contact__list contact__list--direct">
    <li class="contact__item">
      <svg class="contact__icon" viewBox="0 0 20 20" aria-hidden="true">
        <circle cx="10" cy="10" r="8.5" fill="none" stroke="#d9d4de" stroke-width="1.3"/>
        <path d="M7.3 5.8l1.4 1.9-.9 1.1c.6 1.2 1.4 2 2.5 2.5l1.1-.9 1.9 1.4-.8 1.5c-3.4-.3-6.3-3.2-6.6-6.6z" fill="#d9d4de"/>
      </svg>
      <span class="contact__phones"><span>(xx) xxxx-xxxx</span><span>(xx) xxxx-xxxx</span></span>
    </li>
    <li class="contact__item contact__item--email">
      <svg class="contact__icon" viewBox="0 0 20 20" aria-hidden="true">
        <circle cx="10" cy="10" r="8.5" fill="none" stroke="#d9d4de" stroke-width="1.3"/>
        <rect x="5.5" y="7" width="9" height="6.2" fill="none" stroke="#d9d4de" stroke-width="1.1"/>
        <path d="M5.5 7l4.5 3.4 4.5-3.4" fill="none" stroke="#d9d4de" stroke-width="1.1"/>
      </svg>
      <span>seuemail.com</span>
    </li>
  </ul>

  <ul class="contact__list contact__list--social">
    <li class="contact__item">
      <svg class="contact__icon" viewBox="0 0 20 20" aria-hidden="true"><circle cx="10" cy="10" r="8.5" fill="none" stroke="#d9d4de" stroke-width="1.3"/></svg>
      <span>Mural</span>
    </li>
    <li class="contact__item">
      <svg class="contact__icon" viewBox="0 0 20 20" aria-hidden="true"><circle cx="10" cy="10" r="8.5" fill="none" stroke="#d9d4de" stroke-width="1.3"/></svg>
      <span>Vitrine</span>
    </li>
  </ul>
</section>

<section class="card card--brand">
  <div class="brand__mark" aria-hidden="true"></div>
  <h2 class="brand__name">LIA MOREIRA</h2>
  <p class="brand__tagline">DESIGN DE INTERIORES</p>
  <div class="brand__rule"></div>
</section>

</body>
</html>
```